Business card design needed

We are a boutique law firm within the Melbourne CBD.

You will need to upload our company logo which is to go on the left hand side of the business card - we then have a Legal Guild of Carrowmere logo to go perhaps on the bottom right hand side (color)

On the back we would like the website details

www.hartwellsolicitors.com.au - with a small logo
Updates

Thank you designers for all your great submissions.  Just going through the designs and we will choose one within the next couple of days.

Kind Regards
Hartwells Solicitors Pty Ltd

Industry/Entity Type

Boutique

Contact Information for Business Card

Dominic Hartwell
Principal
Level 6, 47 Penrose Street
Melbourne VIC Australia 3000
T+61 3 9555 0142 F+61 3 9555 0187
dominic@hartwellsolicitors.com.au
M 0491 570 156

```html
<!DOCTYPE html>
<html lang="en">
<head>
<meta charset="utf-8">
<title>Hartwells Solicitors – Business Card</title>
<link rel="stylesheet" href="https://fonts.googleapis.com/css2?family=Arimo:wght@700&family=Source+Sans+3:wght@400&display=swap">
<style>
  :root {
    --page: #ffffff;
    --card: #5d8ea4;
    --band: #3b7084;
    --ink: #ffffff;
  }
  * { margin: 0; padding: 0; box-sizing: border-box; }
  html, body {
    width: 1200px;
    height: 1000px;
    overflow: hidden;
    background: var(--page);
  }
  .canvas {
    position: relative;
    width: 1200px;
    height: 1000px;
  }
  .card {
    position: absolute;
    left: 80px;
    top: 202px;
    width: 1041px;
    height: 590px;
    background: var(--card);
    overflow: hidden;
  }
  .card__band {
    position: absolute;
    left: 0;
    top: 148px;
    width: 100%;
    height: 98px;
    background: var(--band);
  }
  .brand {
    position: absolute;
    left: 0;
    top: 0;
    width: 100%;
    height: 100%;
  }
  .brand__square {
    position: absolute;
    left: 344px;
    top: 155px;
    width: 130px;
    height: 130px;
    background: var(--ink);
  }
  .brand__name {
    position: absolute;
    left: 490px;
    top: 205px;
    font-family: "Arimo", Arial, sans-serif;
    font-weight: 700;
    font-size: 88px;
    line-height: 1;
    letter-spacing: -0.5px;
    color: var(--ink);
    white-space: nowrap;
  }
  .contact {
    position: absolute;
    left: 0;
    top: 332px;
    width: 100%;
    text-align: center;
    font-family: "Source Sans 3", "Myriad Pro", sans-serif;
    font-weight: 400;
    font-size: 26px;
    line-height: 42px;
    letter-spacing: -0.2px;
    color: var(--ink);
  }
  .contact__line { display: block; white-space: nowrap; }
  .contact__sep {
    display: inline-block;
    margin: 0 10px;
    font-size: 18px;
    vertical-align: 2px;
  }
</style>
</head>
<body>
  <main class="canvas">
    <section class="card" aria-label="Hartwells Solicitors business card">
      <div class="card__band"></div>
      <div class="brand">
        <span class="brand__square" aria-hidden="true"></span>
        <span class="brand__name">Hartwells</span>
      </div>
      <address class="contact" style="font-style: normal;">
        <span class="contact__line">Dominic Hartwell Principal Hartwells Solicitors Pty Ltd<span class="contact__sep">•</span>Level 6, 47 Penrose Street</span>
        <span class="contact__line">Melbourne VIC Australia 3000<span class="contact__sep">•</span>T: +61 3 9555 0142<span class="contact__sep">•</span>F: +61 3 9555 0187</span>
        <span class="contact__line"><span class="contact__sep">•</span>E: dominic@hartwellsolicitors.com.au<span class="contact__sep">•</span>M: 0491 570 156</span>
      </address>
    </section>
  </main>
</body>
</html>
```